need a Facebook marketing ad for Korvane Welding

www.korvanewelding.example is our website to look at, I need someone to design a 15-30 second ad video/sideshow for a general welding and fabrication shop, tig welding, trailer repair, build staircases, pipe welding. I don't have the media or the artistic abilities to do it. Attached is what I have, fill in the blanks and add to it.

would like to get
1-2 video ads
1-2 graphic ads
1-2 different yard signs

```html
<!DOCTYPE html>
<html lang="en">
<head>
<meta charset="utf-8">
<title>Korvane Welding – Facebook Ad</title>
<link rel="stylesheet" href="https://fonts.googleapis.com/css2?family=Montserrat:ital,wght@0,800;1,500;1,900&family=Roboto+Condensed:wght@700&family=Roboto:ital,wght@1,400;1,700&family=Orbitron:wght@900&display=swap">
<style>
  :root {
    --page: #ffffff;
    --ink: #0b0b0c;
    --panel-dark: #121214;
    --panel-mid: #2a2a2d;
    --red: #e0363a;
    --red-deep: #9c1015;
    --silver-light: #ffffff;
    --silver-dark: #8d8d90;
    --weld-blue: #2c5fd8;
    --white: #ffffff;
  }
  * { box-sizing: border-box; margin: 0; padding: 0; }
  html, body { width: 1200px; height: 1000px; overflow: hidden; background: var(--page); }
  .ad {
    position: absolute; left: 0; top: 162px; width: 1200px; height: 675px;
    overflow: hidden;
    background: linear-gradient(135deg, var(--panel-mid) 0%, var(--panel-dark) 45%, var(--ink) 100%);
  }
  .photo-area {
    position: absolute; left: 0; top: 272px; width: 545px; height: 403px;
    background:
      radial-gradient(ellipse at 40% 85%, rgba(120,170,255,.9) 0%, rgba(44,95,216,.6) 22%, rgba(44,95,216,0) 55%),
      linear-gradient(90deg, #3a3d48 0%, #26272d 55%, rgba(18,18,20,0) 100%);
  }
  .headline-lead {
    position: absolute; left: 66px; top: 48px;
    font: italic 500 58px/1 "Montserrat", sans-serif;
    background: linear-gradient(90deg, var(--red) 0%, #f3b3b5 45%, var(--red) 100%);
    -webkit-background-clip: text; background-clip: text; color: transparent;
  }
  .headline-main {
    position: absolute;
    font: italic 900 72px/1 "Montserrat", sans-serif;
    background: linear-gradient(180deg, var(--silver-light) 20%, var(--silver-dark) 100%);
    -webkit-background-clip: text; background-clip: text; color: transparent;
    letter-spacing: -1px;
  }
  .headline-main.line-one { left: 145px; top: 110px; }
  .headline-main.line-two { left: 200px; top: 185px; }
  .tagline {
    position: absolute; left: 186px; top: 262px;
    font: italic 400 19px/1 "Roboto", sans-serif;
    letter-spacing: 5.6px; color: var(--white);
  }
  .brand {
    position: absolute; left: 848px; top: 100px; width: 240px;
    display: flex; flex-direction: column; align-items: center; gap: 12px;
  }
  .brand-dot { width: 46px; height: 46px; border-radius: 50%; background: var(--red); }
  .brand-name {
    font: 800 32px/1.05 "Montserrat", sans-serif; color: var(--white);
    text-align: center; text-transform: uppercase;
  }
  .services { position: absolute; left: 548px; top: 316px; list-style: none; }
  .service {
    width: 486px; height: 50px; margin-bottom: 22px;
    padding-left: 15px;
    clip-path: polygon(0 0, 466px 0, 486px 100%, 0 100%);
    background: linear-gradient(180deg, var(--red) 0%, var(--red) 50%, var(--red-deep) 100%);
    font: 700 39px/50px "Roboto Condensed", sans-serif; color: var(--white);
    text-shadow: 2px 2px 3px rgba(0,0,0,.5);
  }
  .contact { position: absolute; left: 548px; top: 600px; display: flex; align-items: center; }
  .contact-label {
    font: 800 16px/0.95 "Montserrat", sans-serif; color: var(--white); text-transform: uppercase;
  }
  .contact-icon { width: 40px; height: 40px; margin-left: 16px; }
  .contact-phone {
    margin-left: 6px;
    font: 900 35px/1 "Orbitron", sans-serif; color: var(--white); letter-spacing: 2px;
  }
  .base-strip {
    position: absolute; left: 553px; top: 656px; width: 647px; height: 19px;
    clip-path: polygon(0 0, 100% 0, 100% 100%, 6px 100%);
    background: linear-gradient(90deg, #6f6f72, #dcdcde 60%, #8a8a8d);
  }
</style>
</head>
<body>
  <section class="ad">
    <div class="photo-area" role="img" aria-label="Photo of a welder in a helmet working with bright blue sparks"></div>

    <p class="headline-lead">WE SPECIALIZE IN</p>
    <h1>
      <span class="headline-main line-one">WELDING AND</span>
      <span class="headline-main line-two">FABRICATION</span>
    </h1>
    <p class="tagline">IF YOU CAN DREAM IT, WE CAN BUILD IT</p>

    <div class="brand">
      <span class="brand-dot"></span>
      <span class="brand-name">Korvane<br>Welding</span>
    </div>

    <ul class="services">
      <li class="service">TIG WELDING</li>
      <li class="service">TRAILER REPAIR</li>
      <li class="service">STAIRCASE CONSTRUCTION</li>
      <li class="service">PIPE WELDING</li>
    </ul>

    <div class="contact">
      <p class="contact-label">Free Quote<br>Call Now</p>
      <svg class="contact-icon" viewBox="0 0 40 40" aria-hidden="true">
        <circle cx="20" cy="20" r="18" fill="#e0363a"/>
        <circle cx="20" cy="20" r="12" fill="#ffffff"/>
        <path d="M15 13c1-1 2-1 3 0l1.5 2.5c.4.8 0 1.5-.6 2l-1 .8c.8 1.8 2 3 3.8 3.8l.8-1c.5-.6 1.2-1 2-.6L27 22c1 1 1 2 0 3l-1 1c-5 1-12-6-11-11z" fill="#121214"/>
      </svg>
      <p class="contact-phone">555-014-2270</p>
    </div>

    <div class="base-strip"></div>
  </section>
</body>
</html>
```